Improvement of design for elearning template

Our company provides web based elearning courses for employees. We have a design layout for the different slides which can be found here: https://www.filevault-example.com/sh/qk4rmtp8zy2bnel/BXcQuPeMdKtLwZrnaHv71sGtuQ?dl=0. The content will be added later. At this point we are just looking for a design layout that works with different content types like images, text, quiz & videos. What we would ask you, is to pick randomly 1 or 2 of the elearning slides from the existing designs and suggest improvements or come up with an alternative design. The winner of the design project can work on all slides and this will be a project with a much larger budget.
Target Market(s)
Employees in large enterprises
Look and feel
Each slider illustrates characteristics of the customer's brand and the style your logo design should communicate.

```html
<!DOCTYPE html>
<html lang="en">
<head>
<meta charset="utf-8">
<title>Handling Sensitive Information Course – Landing Slide</title>
<link rel="stylesheet" href="https://fonts.googleapis.com/css2?family=Nunito+Sans:wght@400;600;700;800&display=swap">
<style>
  :root {
    --page-bg: #ededf0;
    --slide-bg: #ffffff;
    --ink: #2f3e54;
    --ink-soft: #4a5568;
    --brand: #6a3fd6;
    --brand-muted: #6a5fb0;
    --underline: #8c7cc9;
    --icon: #8a7bd0;
    --blob: #efeff0;
    --art-pink: #e7a6e4;
    --art-violet: #b766c0;
    --art-grey: #ececee;
  }
  * { box-sizing: border-box; margin: 0; padding: 0; }
  html, body {
    width: 1200px; height: 1200px; overflow: hidden;
    background: var(--page-bg);
    font-family: "Nunito Sans", Arial, sans-serif;
    color: var(--ink);
  }
  .slide {
    position: absolute; left: 0; top: 293px;
    width: 1200px; height: 613px;
    background: var(--slide-bg);
    overflow: hidden;
  }
  .backdrop-wave { position: absolute; left: 0; top: 0; width: 1200px; height: 613px; }

  .brand {
    position: absolute; left: 111px; top: 36px;
    display: flex; align-items: center; gap: 7px;
    font-size: 14px; font-weight: 700; color: var(--ink);
  }
  .brand-dot { width: 14px; height: 14px; border-radius: 50%; background: var(--ink); }

  .nav { position: absolute; top: 36px; left: 0; width: 1200px; height: 25px; }
  .nav-link {
    position: absolute; top: 4px; font-size: 13px; color: var(--ink-soft);
    text-decoration: none;
  }
  .nav-cta {
    position: absolute; left: 997px; top: 0; width: 92px; height: 25px;
    border: 1.5px solid var(--brand); border-radius: 3px;
    color: var(--brand); font-size: 13px; font-weight: 800;
    display: flex; align-items: center; justify-content: center;
  }

  .intro { position: absolute; left: 112px; top: 156px; width: 470px; }
  .intro-eyebrow { font-size: 17px; font-weight: 600; color: var(--brand-muted); line-height: 22px; }
  .intro-title {
    margin-top: 4px;
    font-size: 45px; font-weight: 800; line-height: 54px;
    color: var(--ink); white-space: nowrap;
  }
  .intro-title .accent {
    text-decoration: underline; text-decoration-color: var(--underline);
    text-decoration-thickness: 3px; text-underline-offset: 6px;
  }

  .facts {
    position: absolute; left: 104px; top: 312px; list-style: none;
    display: grid; grid-template-columns: 178px 200px; row-gap: 12px;
  }
  .fact { display: flex; align-items: center; gap: 6px; font-size: 13px; color: var(--ink-soft); height: 22px; }
  .fact svg { width: 13px; height: 13px; flex: none; }

  .cta-start {
    position: absolute; left: 112px; top: 395px; width: 140px; height: 32px;
    background: var(--brand); color: #fff; border-radius: 2px;
    font-size: 17px; font-weight: 700;
    display: flex; align-items: center; justify-content: center;
  }

  .meta { position: absolute; top: 566px; font-size: 13px; color: var(--ink-soft); }
  .meta-year { left: 114px; }
  .meta-version { left: 293px; }

  .hero-art {
    position: absolute; left: 615px; top: 80px; width: 500px; height: 510px;
    border-radius: 46% 46% 50% 50% / 34% 34% 66% 66%;
    background: radial-gradient(ellipse at 45% 42%, var(--art-pink) 0%, var(--art-violet) 42%, var(--art-grey) 80%);
    opacity: 0.85;
  }
</style>
</head>
<body>
  <main class="slide">
    <svg class="backdrop-wave" viewBox="0 0 1200 613" aria-hidden="true">
      <path d="M0 613 V540 C15 488 45 478 90 484 C170 495 250 540 333 555 C410 567 445 575 465 613 Z" fill="var(--blob)"/>
    </svg>

    <div class="brand"><span class="brand-dot"></span>Meridian Secure</div>

    <nav class="nav">
      <a class="nav-link" style="left:711px">Lessons</a>
      <a class="nav-link" style="left:812px">Menu</a>
      <a class="nav-link" style="left:897px">Glossary</a>
      <span class="nav-cta">Learn More</span>
    </nav>

    <section class="intro">
      <p class="intro-eyebrow">Welcome to</p>
      <h1 class="intro-title">Handling <span class="accent">Sensitive</span><br>Information Course</h1>
    </section>

    <ul class="facts">
      <li class="fact">
        <svg viewBox="0 0 14 14" fill="none" stroke="var(--icon)" stroke-width="1.2"><rect x="5" y="0.8" width="4" height="2" rx="0.5"/><rect x="5" y="11.2" width="4" height="2" rx="0.5"/><circle cx="7" cy="7" r="4.3"/><path d="M7 5v2.2l1.3 1"/></svg>
        30 minutes duration
      </li>
      <li class="fact">
        <svg viewBox="0 0 14 14" fill="none" stroke="var(--icon)" stroke-width="1.2"><path d="M1.5 1.5l10 4-4 1.5-1.5 4z"/><path d="M7.5 7l4 4"/></svg>
        Interactive Lessons
      </li>
      <li class="fact">
        <svg viewBox="0 0 14 14" fill="none" stroke="var(--icon)" stroke-width="1.2"><path d="M2.5 1v12M7 1v12M11.5 1v12"/><path d="M1 9h3M5.5 4h3M10 7h3"/></svg>
        Medium Complexity
      </li>
      <li class="fact">
        <svg viewBox="0 0 14 14" fill="none" stroke="var(--icon)" stroke-width="1.2"><circle cx="5" cy="4.5" r="2.3"/><path d="M1 12c0-2.5 1.8-4 4-4s4 1.5 4 4"/><circle cx="10" cy="4" r="1.8"/><path d="M10.5 7.5c1.5.3 2.5 1.6 2.5 3.5"/></svg>
        For all audiences
      </li>
    </ul>

    <div class="cta-start">Get Started</div>

    <p class="meta meta-year">Year Created: 2019</p>
    <p class="meta meta-version">Version 1.1</p>

    <div class="hero-art" role="img" aria-label="Isometric illustration of an employee at a desk with a laptop in front of a large browser window showing folders and a padlock password screen, with a chair, plant and window"></div>
  </main>
</body>
</html>
```